Carpet cleaning company wants business card

Need an exciting new fresh design for business cards for my carpet cleaning /pest control business
www.tidewellhomecare.com.au
Can design include a lined section for quoting or information? Thanks !

```html
<!DOCTYPE html>
<html lang="en">
<head>
<meta charset="utf-8">
<title>Tidewell Home Care – Business Card</title>
<link rel="stylesheet" href="https://fonts.googleapis.com/css2?family=Cabin:wght@400;500;600;700&family=Cabin+Condensed:wght@500;600&display=swap">
<style>
  :root {
    --brand-blue: #0556a4;
    --ink-blue: #0d4aa0;
    --brand-red: #ef3b36;
    --paper: #ffffff;
    --backdrop: #d3d4d6;
    --rule: #333333;
  }
  * { margin: 0; padding: 0; box-sizing: border-box; }
  html, body {
    width: 900px; height: 1200px; overflow: hidden;
    background: var(--backdrop);
    font-family: "Cabin", sans-serif;
  }
  .card {
    position: absolute;
    left: 133px;
    width: 633px;
    height: 364px;
    overflow: hidden;
  }

  /* Front */
  .card--front { top: 210px; background: var(--brand-blue); }
  .front__brand {
    position: absolute; top: 138px; left: 0; width: 100%;
    text-align: center;
    font: 700 50px/1 "Cabin", sans-serif;
    color: var(--paper);
    letter-spacing: -0.5px;
  }
  .front__service {
    position: absolute; top: 240px; left: 0; width: 100%;
    text-align: center;
    font: 600 36px/1 "Cabin Condensed", sans-serif;
    color: var(--brand-red);
    letter-spacing: 0.8px;
  }
  .front__tagline {
    position: absolute; top: 285px; left: 0; width: 100%;
    text-align: center;
    font: 500 14px/1 "Cabin Condensed", sans-serif;
    color: var(--paper);
  }
  .front__form {
    position: absolute; top: 320px; left: 0; width: 100%; height: 31px;
    background: var(--paper);
    display: flex; align-items: center;
    padding: 0 34px;
    font: 500 16px/1 "Cabin", sans-serif;
    color: var(--brand-red);
    gap: 6px;
  }
  .form__field { display: flex; align-items: center; gap: 4px; }
  .form__line {
    display: inline-block; height: 2px; margin-top: 9px;
    border-bottom: 2px dotted var(--brand-blue);
  }

  /* Back */
  .card--back { top: 624px; background: var(--paper); }
  .back__brand {
    position: absolute; left: 36px; top: 164px; width: 270px;
    text-align: center;
    font: 700 34px/1 "Cabin", sans-serif;
    color: var(--ink-blue);
    letter-spacing: -0.3px;
  }
  .back__divider {
    position: absolute; left: 327px; top: 107px;
    width: 1.5px; height: 153px; background: var(--rule);
  }
  .back__contact { position: absolute; left: 348px; top: 102px; }
  .contact__name {
    font: 600 25px/1 "Cabin", sans-serif;
    color: var(--brand-red);
    letter-spacing: 0.5px;
  }
  .contact__role {
    margin-top: 6px;
    font: 400 15px/1 "Cabin", sans-serif;
    color: var(--ink-blue);
  }
  .contact__list { list-style: none; margin-top: 20px; }
  .contact__item {
    display: flex; align-items: center; gap: 6px;
    height: 24.5px;
    font: 500 14px/1 "Cabin", sans-serif;
    color: var(--ink-blue);
  }
  .contact__item--spaced { letter-spacing: 2.4px; font-size: 15px; }
  .contact__item--web { letter-spacing: 0.5px; }
  .contact__icon { width: 15px; height: 15px; flex: none; }
  .back__hours {
    position: absolute; left: 0; top: 306px; width: 100%;
    text-align: center;
    font: 500 17px/1 "Cabin", sans-serif;
    color: var(--ink-blue);
  }
  .hours__label { color: var(--brand-red); }
</style>
</head>
<body>

<section class="card card--front">
  <div class="front__brand">Tidewell Home Care</div>
  <div class="front__service">Carpet Cleaning Cairns</div>
  <div class="front__tagline">Enjoy a Fresh, Clean Environment the Tidewell Way</div>
  <div class="front__form">
    <span class="form__field">Name: <span class="form__line" style="width:202px"></span></span>
    <span class="form__field">Time: <span class="form__line" style="width:92px"></span></span>
    <span class="form__field">Date: <span class="form__line" style="width:114px"></span></span>
  </div>
</section>

<section class="card card--back">
  <div class="back__brand">Tidewell Home Care</div>
  <div class="back__divider"></div>
  <div class="back__contact">
    <div class="contact__name">JOHN DOE</div>
    <div class="contact__role">Installer</div>
    <ul class="contact__list">
      <li class="contact__item contact__item--spaced">
        <svg class="contact__icon" viewBox="0 0 16 16" aria-hidden="true"><path fill="#ef3b36" d="M3.6 1.2l2.3 2.6-1.3 1.9c.9 2 2.5 3.6 4.6 4.6l1.9-1.3 2.6 2.3-1.2 2.4C7.3 13.7 2.3 8.7 1.2 3.4z"/></svg>
        07 4000 2815
      </li>
      <li class="contact__item contact__item--spaced">
        <svg class="contact__icon" viewBox="0 0 16 16" aria-hidden="true"><rect x="4" y="1" width="8" height="14" rx="1.5" fill="none" stroke="#ef3b36" stroke-width="1.6"/><circle cx="8" cy="12.4" r="0.9" fill="#ef3b36"/></svg>
        0400 562 913
      </li>
      <li class="contact__item">
        <svg class="contact__icon" viewBox="0 0 16 16" aria-hidden="true"><rect x="1" y="3.5" width="14" height="9.5" fill="#ef3b36"/><path d="M1.5 4l6.5 5 6.5-5M1.5 12.5l5-4.2M14.5 12.5l-5-4.2" stroke="#fff" stroke-width="1.1" fill="none"/></svg>
        admin@tidewellhomecare.com.au
      </li>
      <li class="contact__item contact__item--web">
        <svg class="contact__icon" viewBox="0 0 16 16" aria-hidden="true"><g fill="none" stroke="#ef3b36" stroke-width="1.3"><circle cx="8" cy="8" r="6.5"/><ellipse cx="8" cy="8" rx="2.8" ry="6.5"/><path d="M1.5 8h13M2.5 4.8h11M2.5 11.2h11"/></g></svg>
        www.tidewellhomecare.com.au
      </li>
    </ul>
  </div>
  <div class="back__hours"><span class="hours__label">Hours:</span> Mon to Fri 8:00am to 6:00pm</div>
</section>

</body>
</html>
```